We need a business card design for a new company based in
Perth, Western Australia called Oveko Tiling Services. We specialize in laying Wall and Floor Tiles and Stone. We expertise in all small to large format tiles and do good quality work. Sincerity and Convition is what seperates us from others.

```html
<!DOCTYPE html>
<html lang="en">
<head>
<meta charset="utf-8">
<title>Oveko Tiling Services – Business Card</title>
<link href="https://fonts.googleapis.com/css2?family=Cinzel:wght@400;600&family=Roboto:wght@400&display=swap" rel="stylesheet">
<style>
  :root {
    --stage: #2f363b;
    --card-top: #e6e6e6;
    --card-bottom: #ffffff;
    --gold: #a8863a;
    --gold-soft: #c9a965;
    --gold-pale: #ead9b8;
    --ink: #2b2b2b;
  }
  * { box-sizing: border-box; margin: 0; padding: 0; }
  html, body { width: 1200px; height: 661px; overflow: hidden; }
  body { background: var(--stage); position: relative; font-family: "Cinzel", serif; }

  .card {
    position: absolute; top: 158px; width: 557px; height: 343px;
    background: linear-gradient(to bottom, var(--card-top), var(--card-bottom));
    overflow: hidden;
  }
  .card--front { left: 27px; }
  .card--back { left: 615px; }

  .mosaic { position: absolute; }
  .card--front .mosaic {
    right: 0; top: 0; width: 300px; height: 245px;
    background: radial-gradient(ellipse at 75% 40%, rgba(168,134,58,0.85), rgba(201,169,101,0.45) 45%, rgba(201,169,101,0) 72%);
  }
  .card--back .mosaic {
    right: 0; top: 0; width: 200px; height: 240px;
    background: radial-gradient(ellipse at 70% 45%, rgba(234,217,184,0.95), rgba(234,217,184,0.4) 50%, rgba(234,217,184,0) 75%);
  }

  .brand { position: absolute; color: var(--gold); }
  .brand__name { font-family: "Cinzel", serif; font-weight: 600; font-size: 25px; letter-spacing: 0.5px; line-height: 1; }
  .brand__tagline { font-family: "Cinzel", serif; font-size: 12px; letter-spacing: 0.6px; margin-top: 8px; }
  .card--front .brand { left: 40px; top: 70px; }
  .card--back .brand { left: 0; right: 0; top: 128px; text-align: center; }

  .location { position: absolute; left: 41px; top: 243px; font-size: 15px; color: var(--ink); letter-spacing: 0.4px; }
  .contact { position: absolute; left: 39px; top: 279px; list-style: none; font-family: "Roboto", sans-serif; font-size: 15px; color: var(--ink); }
  .contact li { display: flex; align-items: center; gap: 8px; height: 21px; }
  .contact svg { width: 11px; height: 11px; }

  .services { position: absolute; left: 20px; right: 20px; top: 253px; text-align: center; color: var(--ink); font-size: 13.5px; line-height: 21px; }
  .services span::before { content: "•"; color: var(--gold-soft); margin: 0 5px 0 8px; }
  .services__rule { position: absolute; left: 20px; right: 20px; top: 297px; height: 1px; background: var(--gold-soft); }
  .services__note { position: absolute; left: 0; right: 0; top: 301px; text-align: center; font-size: 13px; color: var(--ink); letter-spacing: 0.3px; }
</style>
</head>
<body>
  <section class="card card--front">
    <div class="mosaic" role="img" aria-label="Gold triangle tile mosaic"></div>
    <div class="brand">
      <div class="brand__name">Oveko Tiling Services</div>
      <div class="brand__tagline">Sincerity &amp; Conviction</div>
    </div>
    <p class="location">Perth, Western Australia</p>
    <ul class="contact">
      <li>
        <svg viewBox="0 0 11 11" aria-hidden="true"><rect x="2.5" y="0.5" width="6" height="10" rx="1" fill="none" stroke="#a8863a"/><rect x="4.5" y="8.3" width="2" height="1" fill="#a8863a"/></svg>
        0400 123 456
      </li>
      <li>
        <svg viewBox="0 0 11 11" aria-hidden="true"><rect x="0.5" y="2" width="10" height="7" fill="none" stroke="#a8863a"/><path d="M0.5 2 L5.5 6 L10.5 2" fill="none" stroke="#a8863a"/></svg>
        hello@ovekotiling.com
      </li>
    </ul>
  </section>

  <section class="card card--back">
    <div class="mosaic" role="img" aria-label="Faint gold triangle tile mosaic"></div>
    <div class="brand">
      <div class="brand__name">Oveko Tiling Services</div>
      <div class="brand__tagline">Sincerity &amp; Conviction</div>
    </div>
    <p class="services">
      <span>Free Quote</span><span>Large Format Porcelain</span><span>Natural Stone &amp; Granite</span><br>
      <span>Interior Feature Walls</span><span>Exterior Elevations</span>
    </p>
    <div class="services__rule"></div>
    <p class="services__note">We also offer a design and install service</p>
  </section>
</body>
</html>
```